Realtor/Real Estate Investor Business Card Design

We need a business card design for a new real estate company in Maryland. We buy houses, fix and sell. We do wholesaling as well. We also rent houses.We would like to have blue background and white font.
Updates

Hi All,
I thank all of you for your efforts. You are all experts in designing.
Looking forward to meeting you online in the near future.
mira

Industry/Entity Type

Real Estate

Contact Information for Business Card

Mira Talwen
Real Estate Professional
mira@brightkeyhomes.com
301-584-3092
Bright K Homes.com

Requirements
Must have
• House picture, and logo at the back of the card
We simplify your buying and selling real estate. at the back of the card

```html
<!DOCTYPE html>
<html lang="en">
<head>
<meta charset="utf-8">
<title>Mira Talwen – Business Card</title>
<link rel="stylesheet" href="https://fonts.googleapis.com/css2?family=Arimo:wght@700&family=Tinos&display=swap">
<style>
  :root {
    --page-bg: #e6e6e8;
    --card-white: #ffffff;
    --blue-light: #35499c;
    --blue-dark: #211b5e;
    --navy: #2a2a72;
    --band-black: #1c1c1f;
    --tag-grey: #555559;
    --text-white: #ffffff;
  }
  * { margin: 0; padding: 0; box-sizing: border-box; }
  html, body {
    width: 1200px;
    height: 1200px;
    overflow: hidden;
    background: var(--page-bg);
  }
  .sheet {
    position: relative;
    width: 1200px;
    height: 1200px;
  }
  .card {
    position: absolute;
    top: 451px;
    width: 540px;
    height: 298px;
    overflow: hidden;
    box-shadow: 0 6px 18px rgba(0,0,0,0.18);
  }
  .card-front { left: 40px; background: var(--card-white); }
  .card-back {
    left: 620px;
    background: linear-gradient(90deg, var(--blue-light) 0%, var(--blue-dark) 100%);
  }
  .front-shapes { position: absolute; inset: 0; }

  .brand {
    position: absolute;
    text-align: center;
  }
  .brand-line {
    display: flex;
    align-items: center;
    gap: 8px;
    justify-content: center;
  }
  .brand-mark {
    width: 14px;
    height: 14px;
  }
  .brand-name {
    font-family: "Arimo", Arial, sans-serif;
    font-weight: 700;
    font-size: 27px;
    letter-spacing: 0.3px;
  }
  .brand-tagline {
    font-family: "Tinos", "Times New Roman", serif;
    font-size: 16px;
    margin-top: 2px;
  }

  .card-front .brand { left: 22px; top: 130px; width: 200px; }
  .card-front .brand-mark { background: var(--navy); }
  .card-front .brand-name { color: var(--navy); }
  .card-front .brand-tagline { color: var(--tag-grey); }

  .card-back .brand { left: 0; right: 0; top: 132px; }
  .card-back .brand-mark { background: var(--text-white); }
  .card-back .brand-name { color: var(--text-white); }
  .card-back .brand-tagline { color: #d9dcf0; }

  .contact-list {
    position: absolute;
    right: 30px;
    top: 178px;
    list-style: none;
    font-family: "Arimo", Arial, sans-serif;
    font-weight: 700;
    color: var(--text-white);
    text-align: right;
  }
  .contact-item {
    display: flex;
    justify-content: flex-end;
    align-items: center;
    gap: 9px;
    line-height: 22px;
  }
  .contact-item.phone { font-size: 16px; }
  .contact-item.web, .contact-item.mail { font-size: 14.5px; }
  .contact-icon { width: 13px; height: 13px; flex: none; }
</style>
</head>
<body>
<main class="sheet">

  <section class="card card-front" aria-label="Card front">
    <svg class="front-shapes" viewBox="0 0 540 298" width="540" height="298" aria-hidden="true">
      <defs>
        <linearGradient id="frontBlue" x1="0" y1="0" x2="1" y2="0">
          <stop offset="0" stop-color="#35499c"/>
          <stop offset="1" stop-color="#211b5e"/>
        </linearGradient>
      </defs>
      <polygon points="268,100 302,100 244,298 206,298" fill="#1c1c1f"/>
      <polygon points="331,0 540,0 540,298 244,298" fill="url(#frontBlue)"/>
    </svg>

    <div class="brand">
      <div class="brand-line">
        <span class="brand-mark"></span>
        <span class="brand-name">Mira Talwen</span>
      </div>
      <div class="brand-tagline">Real Estate Professional</div>
    </div>

    <ul class="contact-list">
      <li class="contact-item phone">301-584-3092
        <svg class="contact-icon" viewBox="0 0 16 16" aria-hidden="true"><rect x="0" y="0" width="16" height="16" rx="3" fill="#fff"/><path d="M5 3.5c-.8.4-1.3 1.3-1 2.3.8 2.7 2.9 4.9 5.6 5.9 1 .3 2-.2 2.4-1l-1.9-1.5-1.2.8c-1.1-.6-2-1.5-2.6-2.6l.8-1.2z" fill="#2a2a72"/></svg>
      </li>
      <li class="contact-item web">Bright K Homes.com
        <svg class="contact-icon" viewBox="0 0 16 16" aria-hidden="true"><circle cx="8" cy="8" r="6.5" fill="none" stroke="#fff" stroke-width="1.4"/><ellipse cx="8" cy="8" rx="2.8" ry="6.5" fill="none" stroke="#fff" stroke-width="1.2"/><path d="M1.5 8h13" stroke="#fff" stroke-width="1.2"/></svg>
      </li>
      <li class="contact-item mail">mira@brightkeyhomes.com
        <svg class="contact-icon" viewBox="0 0 16 16" aria-hidden="true"><rect x="1" y="3" width="14" height="10" rx="1" fill="#fff"/><path d="M1.5 3.5 8 9l6.5-5.5" fill="none" stroke="#2a2a72" stroke-width="1.3"/></svg>
      </li>
    </ul>
  </section>

  <section class="card card-back" aria-label="Card back">
    <div class="brand">
      <div class="brand-line">
        <span class="brand-mark"></span>
        <span class="brand-name">Mira Talwen</span>
      </div>
      <div class="brand-tagline">Real Estate Professional</div>
    </div>
  </section>

</main>
</body>
</html>
```